Save the Date for a Virtual Gala Event: Footlights at Home

We need an eblast that can be loaded to Mailchimp, which will serve as the Save the Date for an event taking place in 2021. It was also be the first material for the event and so will serve as the look and feel for future materials such as a web landing page and invitation. The content is as follows:

Save the Date

This Valentine’s Weekend 2021

Allies of the Youngsters New York

is bringing Broadway into your home

Friday, February 12, 2021

Hosted by
Marlow Award Winning Broadway Star Dora Pemberton

Additional celebrity guests to be announced in early 2021.

Vidmeet doors open at 7 pm
The show will begin promptly at 7:30 pm

For early registration information, contact Margo Vance at mvance@alliesmentoring.example.

Allies Eblast Footer and Logo

Allies of the Youngsters New York is a 501c3 nonprofit organization that is breaking the cycle of generational poverty by pairing children facing multiple systemic obstacles with a long-term, salaried, professional mentor, called a Friend, from kindergarten through high school graduation – 12 + years, no matter what. Allies of the Youngsters New York is committed to providing the necessary opportunities, resources, and social supports for the black and brown community to thrive.

AlliesMentoring.example

1. Allies NY Branding Guide...Provided to show our typical colors and fonts but it is ok to improvise to fit the event (gold glitter, or red carpet, or a Stagecard or anything that supports the Broadway theme).
2. Allies logos
3. Dora Pemberton Photo (only if it fits your design)

We would like to see additional entries.

Target Market(s)

Wealthy New York City donors who are missing Broadway during quarantine and want to hear live Broadway performances over Vidmeet while supporting an amazing non profit organization/charity.

Requirements
Must have
• The date and theme (Footlights at home)
Nice to have
• A photo of Allies of the Youngsters New York's work incorporated in the footer if it fits

We like elements the sparkly Broadway headers or theaters we have seen so far.
Should not have
• No hearts. We do not want the design to be too busy.

If photos of the Allies of the Youngsters New York children with mentors are used, they should be at the bottom near the description of Allies of the Youngsters New York and our logo.

```html
<!DOCTYPE html>
<html lang="en">
<head>
<meta charset="utf-8">
<title>Save the Date – Footlights at Home</title>
<link href="https://fonts.googleapis.com/css2?family=Montserrat:wght@400;500;600;800;900&family=Yellowtail&display=swap" rel="stylesheet">
<style>
:root{
  --ink:#000;
  --paper:#fff;
  --gold-light:#f0c62a;
  --gold-mid:#c98f1c;
  --gold-dark:#8a4a17;
  --footer-ink:#1e1e1e;
  --logo-grey:#58595b;
}
*{margin:0;padding:0;box-sizing:border-box}
html,body{width:715px;height:1200px;overflow:hidden;background:var(--paper)}
body{font-family:"Montserrat",sans-serif;color:var(--paper)}
.eblast{position:relative;width:715px;height:1200px;background:var(--paper)}
.hero{position:absolute;left:0;top:0;width:715px;height:853px;background:var(--ink);overflow:hidden}
.host-photo{position:absolute;left:380px;top:0;width:335px;height:853px;
  background:radial-gradient(ellipse at 62% 30%,#6b4a3a 0%,#3a2620 30%,#1a120f 60%,#000 100%)}
.glow{position:absolute;left:0;top:745px;width:560px;height:30px;
  background:radial-gradient(ellipse at 48% 50%,rgba(255,190,90,.55) 0%,rgba(200,110,30,.2) 35%,rgba(0,0,0,0) 70%)}
.script{font-family:"Yellowtail",cursive;position:absolute;line-height:1;
  background:linear-gradient(180deg,var(--gold-light) 0%,var(--gold-mid) 55%,var(--gold-dark) 100%);
  -webkit-background-clip:text;background-clip:text;color:transparent}
.title-save{left:22px;top:8px;font-size:200px}
.title-the{left:196px;top:212px;font-size:54px}
.title-date{left:42px;top:226px;font-size:185px}
.date-pill{position:absolute;left:42px;top:398px;width:403px;height:38px;border-radius:19px;
  background:linear-gradient(90deg,var(--gold-light),var(--gold-mid) 55%,var(--gold-dark));
  font-weight:800;font-size:23px;letter-spacing:.6px;line-height:38px;padding-left:22px}
.lede{position:absolute;left:46px;top:451px;font-weight:800;font-size:16px;line-height:20px;letter-spacing:1px}
.gold-rule{position:absolute;left:45px;width:300px;height:7px;
  background:linear-gradient(90deg,var(--gold-light),var(--gold-mid) 50%,var(--gold-dark))}
.rule-one{top:517px}
.rule-two{top:689px}
.hosted-by{left:41px;top:537px;font-size:25px}
.host{position:absolute;left:49px;top:572px;font-weight:800;font-size:15.5px;line-height:20px;letter-spacing:1px}
.guests{position:absolute;left:49px;top:632px;font-weight:500;font-size:15.5px;line-height:20px;letter-spacing:1.2px}
.showtime{position:absolute;left:51px;top:706px;font-weight:800;font-size:15.5px;line-height:20px;letter-spacing:1px}
.rsvp-pill{position:absolute;left:49px;top:763px;width:354px;height:69px;border-radius:16px;
  background:linear-gradient(90deg,var(--gold-light),var(--gold-mid) 55%,var(--gold-dark));
  font-weight:800;font-size:15px;line-height:20px;letter-spacing:.5px;text-align:center;padding-top:4px}
.footer-logo{position:absolute;left:49px;top:884px;width:215px;font-weight:600;color:var(--logo-grey);
  font-size:21px;line-height:26px;letter-spacing:1.5px}
.footer-about{position:absolute;left:276px;top:884px;width:396px;color:var(--footer-ink);
  font-size:10.3px;line-height:12.8px;letter-spacing:.5px;font-weight:400}
</style>
</head>
<body>
<main class="eblast">
  <section class="hero">
    <div class="host-photo" role="img" aria-label="Portrait of host Dora Pemberton in a black leather jacket, framed by gold glitter"></div>
    <div class="glow"></div>
    <h1>
      <span class="script title-save">Save</span>
      <span class="script title-the">the</span>
      <span class="script title-date">Date</span>
    </h1>
    <div class="date-pill">FRIDAY, FEBRUARY 12, 2021</div>
    <p class="lede">ALLIES OF THE YOUNGSTERS NEW YORK<br>IS BRINGING BROADWAY INTO YOUR HOME<br>THIS VALENTINE’S WEEKEND 2021</p>
    <div class="gold-rule rule-one"></div>
    <p class="script hosted-by">Hosted By</p>
    <p class="host">MARLOW AWARD WINNING<br>BROADWAY STAR DORA PEMBERTON</p>
    <p class="guests">ADDITIONAL CELEBRITY GUESTS<br>TO BE ANNOUNCED IN EARLY 2021.</p>
    <div class="gold-rule rule-two"></div>
    <p class="showtime">VIDMEET DOORS OPEN AT 7 PM<br>THE SHOW WILL BEGIN PROMPTLY AT 7:30 PM</p>
    <p class="rsvp-pill">For early registration information,<br>contact Margo Vance at<br>mvance@alliesmentoring.example.</p>
  </section>
  <footer>
    <p class="footer-logo">ALLIES of the YOUNGSTERS New York</p>
    <p class="footer-about">Allies of the Youngsters New York is a 501c3 nonprofit organization that is breaking the cycle of generational poverty by pairing children facing multiple systemic obstacles with a long-term, salaried, professional mentor, called a Friend, from kindergarten through high school graduation – 12 + years, no matter what. Allies of the Youngsters New York is committed to providing the necessary opportunities, resources, and social supports for the black and brown community to thrive.</p>
  </footer>
</main>
</body>
</html>
```